Stationery Design for Family Law Firm
BROOK VESTAL, LLP
Stationery Design for Family Law Firm -
Creative Brief
Professional
Martin D. Vestal
Attorney & Counselor at Law
4187 Larkin Street San Diego, CA 92104
martin@brookvestal-law.example
www.brookvestal-law.example
Paper will be ivory. Please use large and small caps for name and "Attorney & Counselor" at Law. Sentence case for the rest.
Family Law I Guardianships I Conservatorships I Estate Planning

```html
<!DOCTYPE html>
<html lang="en">
<head>
<meta charset="utf-8">
<title>Brook Vestal, LLP — Stationery</title>
<link rel="stylesheet" href="https://fonts.googleapis.com/css2?family=Cormorant+Garamond:wght@500;600&family=Cormorant+SC:wght@500;600&display=swap">
<style>
  :root {
    --backdrop: #e7e4de;
    --paper: #fdfbf5;
    --paper-edge: #e2ddd2;
    --ink: #232a33;
    --ink-soft: #6c7480;
    --accent: #3a8fc4;
    --dark-card: #15181c;
    --dark-card-2: #1e2329;
    --dark-text: #d9dde2;
  }
  * { box-sizing: border-box; margin: 0; padding: 0; }
  html, body { width: 1200px; height: 677px; overflow: hidden; }
  body {
    background: var(--backdrop);
    font-family: "Cormorant Garamond", Georgia, serif;
    color: var(--ink);
    position: relative;
  }
  .sheet { position: absolute; box-shadow: 0 2px 6px rgba(0,0,0,.18); }

  /* brand lockup */
  .lockup { display: flex; align-items: center; gap: 6px; }
  .lockup-dot { width: 12px; height: 12px; border-radius: 50%; background: var(--accent); flex: none; }
  .lockup-name {
    font-family: "Cormorant SC", Georgia, serif;
    font-weight: 600; color: var(--ink); letter-spacing: .04em; white-space: nowrap;
  }
  .lockup-tag {
    font-family: "Cormorant SC", Georgia, serif;
    font-size: 7px; color: var(--accent); letter-spacing: .05em; margin-top: 2px;
  }

  /* business cards */
  .card { left: 150px; width: 206px; height: 112px; padding: 12px 14px; background: var(--paper); }
  .card-front-light { top: 88px; }
  .card-back-light  { top: 208px; }
  .card-front-dark  { top: 340px; background: linear-gradient(135deg, var(--dark-card-2), var(--dark-card)); }
  .card-back-dark   { top: 460px; background: linear-gradient(135deg, var(--dark-card-2), var(--dark-card)); }

  .card-front { display: flex; flex-direction: column; justify-content: space-between; }
  .card-front .lockup-name { font-size: 11px; }
  .card-person { text-align: right; }
  .card-person-name { font-family: "Cormorant SC", Georgia, serif; font-size: 10px; font-weight: 600; }
  .card-person-role { font-family: "Cormorant SC", Georgia, serif; font-size: 6.5px; color: var(--accent); }
  .card-contact { font-size: 6.5px; line-height: 1.35; color: var(--ink-soft); text-align: right; }
  .card-front-dark .lockup-name,
  .card-front-dark .card-person-name { color: var(--dark-text); }
  .card-front-dark .card-contact { color: #9aa2ab; }

  .card-back { display: flex; flex-direction: column; justify-content: center; }
  .practice-list {
    list-style: none; border-left: 1px solid var(--accent); padding-left: 8px;
    font-family: "Cormorant SC", Georgia, serif; font-size: 8px; line-height: 1.55; color: var(--ink-soft);
  }
  .card-back-dark .practice-list { color: var(--dark-text); }
  .card-web { position: absolute; right: 12px; bottom: 9px; font-size: 6.5px; color: var(--accent); }

  /* letterhead */
  .letterhead { left: 405px; top: 92px; width: 345px; height: 490px; background: var(--paper); padding: 26px 26px; }
  .letterhead-head { display: flex; justify-content: space-between; align-items: flex-start; }
  .letterhead .lockup-name { font-size: 17px; }
  .letterhead .lockup-dot { width: 16px; height: 16px; }
  .letterhead .lockup-tag { font-size: 7px; margin-left: 22px; }
  .letterhead-contact { font-size: 7px; line-height: 1.4; color: var(--ink-soft); text-align: left; width: 120px; }
  .letterhead-rule { margin-top: 14px; height: 1px; background: var(--paper-edge); }

  /* envelopes */
  .envelope { left: 770px; width: 370px; height: 160px; background: var(--paper); overflow: hidden; }
  .envelope svg { position: absolute; inset: 0; }
  .envelope-back-dark  { top: 92px; }
  .envelope-back-light { top: 272px; }
  .envelope-front      { top: 452px; padding: 16px 18px; }
  .envelope-seal { position: absolute; left: 50%; width: 18px; height: 18px; margin-left: -9px; border-radius: 50%; background: var(--accent); }
  .envelope-back-dark .envelope-seal { top: 44px; }
  .envelope-back-light .envelope-seal { top: 50px; }
  .envelope-front .lockup-name { font-size: 13px; }
  .envelope-front .lockup-tag { margin-left: 18px; }
  .envelope-return { font-size: 7px; color: var(--ink-soft); margin-top: 4px; margin-left: 18px; }
</style>
</head>
<body>

  <!-- business cards -->
  <section class="sheet card card-front card-front-light">
    <div>
      <div class="lockup"><span class="lockup-dot"></span><span class="lockup-name">Brook Vestal, LLP</span></div>
      <div class="lockup-tag">Attorney &amp; Counselor at Law</div>
    </div>
    <div>
      <div class="card-person">
        <div class="card-person-name">Martin D. Vestal</div>
        <div class="card-person-role">Attorney &amp; Counselor at Law</div>
      </div>
      <div class="card-contact">4187 Larkin Street San Diego, CA 92104<br>Phone (619) 555-0142<br>martin@brookvestal-law.example</div>
    </div>
  </section>

  <section class="sheet card card-back card-back-light">
    <ul class="practice-list">
      <li>Family Law</li><li>Guardianships</li><li>Conservatorships</li><li>Estate Planning</li>
    </ul>
    <span class="card-web">www.brookvestal-law.example</span>
  </section>

  <section class="sheet card card-front card-front-dark">
    <div>
      <div class="lockup"><span class="lockup-dot"></span><span class="lockup-name">Brook Vestal, LLP</span></div>
      <div class="lockup-tag">Attorney &amp; Counselor at Law</div>
    </div>
    <div>
      <div class="card-person">
        <div class="card-person-name">Martin D. Vestal</div>
        <div class="card-person-role">Attorney &amp; Counselor at Law</div>
      </div>
      <div class="card-contact">4187 Larkin Street San Diego, CA 92104<br>Phone (619) 555-0142<br>martin@brookvestal-law.example</div>
    </div>
  </section>

  <section class="sheet card card-back card-back-dark">
    <ul class="practice-list">
      <li>Family Law</li><li>Guardianships</li><li>Conservatorships</li><li>Estate Planning</li>
    </ul>
    <span class="card-web">www.brookvestal-law.example</span>
  </section>

  <!-- letterhead -->
  <section class="sheet letterhead">
    <header class="letterhead-head">
      <div>
        <div class="lockup"><span class="lockup-dot"></span><span class="lockup-name">Brook Vestal, LLP</span></div>
        <div class="lockup-tag">Attorney &amp; Counselor at Law</div>
      </div>
      <div class="letterhead-contact">4187 Larkin Street<br>San Diego, CA 92104<br>Phone (619) 555-0142<br><br>www.brookvestal-law.example</div>
    </header>
    <div class="letterhead-rule"></div>
  </section>

  <!-- envelopes -->
  <section class="sheet envelope envelope-back-dark">
    <svg width="370" height="160" viewBox="0 0 370 160" aria-hidden="true">
      <path d="M0 160 L150 70 L220 70 L370 160 Z" fill="none" stroke="var(--paper-edge)"/>
      <path d="M0 0 H370 L195 88 Q185 93 175 88 Z" fill="var(--dark-card)"/>
    </svg>
    <span class="envelope-seal"></span>
  </section>

  <section class="sheet envelope envelope-back-light">
    <svg width="370" height="160" viewBox="0 0 370 160" aria-hidden="true">
      <path d="M0 160 L150 70 L220 70 L370 160 Z" fill="none" stroke="var(--paper-edge)"/>
      <path d="M0 0 H370 L195 92 Q185 97 175 92 Z" fill="var(--paper)" stroke="var(--paper-edge)"/>
    </svg>
    <span class="envelope-seal"></span>
  </section>

  <section class="sheet envelope envelope-front">
    <div class="lockup"><span class="lockup-dot"></span><span class="lockup-name">Brook Vestal, LLP</span></div>
    <div class="lockup-tag">Attorney &amp; Counselor at Law</div>
    <div class="envelope-return">4187 Larkin Street San Diego, CA 92104</div>
  </section>

</body>
</html>
```